Bourbon label design for bourbon brand. Looking to freshen our current label.

I need a Bourbon label design for our rebranded Bourbon bottle. Label should include picture of our horse and our logo on the bottle. Front Label is 3.5 inches wide and 6 inches tall, back label is 4 inches tall and 3 inches wide. Back label can be a simple plain logo like the one in the brief. I have included a design of our current bottle and label. We want to stay close to the current color schemes but want a fresh rebrand of the design. The label needs to be the correct size on a tall bottle like pictured.

Target Market(s)

Our Bourbon members, 30-50 year old males

Requirements
Must have
• Picture of our horse, our B logo , straight Bourbon whiskey on the front. Room to edit text on the back label.

```html
<!DOCTYPE html>
<html lang="en">
<head>
<meta charset="utf-8">
<title>Darkrun Straight Bourbon Whiskey – Front Label</title>
<link href="https://fonts.googleapis.com/css2?family=Abril+Fatface&family=Pinyon+Script&family=Roboto+Slab:wght@500;700&display=swap" rel="stylesheet">
<style>
  :root {
    --backdrop: #c8c3c8;
    --label-black: #1b1a1c;
    --label-black-soft: #26252a;
    --copper: #c39a78;
    --cream: #f3eee6;
    --horse-light: #bdbcbc;
    --horse-dark: #4a4a4c;
  }
  * { margin: 0; padding: 0; box-sizing: border-box; }
  html, body {
    width: 1200px; height: 1198px; overflow: hidden;
    background: var(--backdrop);
  }
  .label {
    position: absolute; left: 320px; top: 119px;
    width: 560px; height: 960px; overflow: hidden;
    background: radial-gradient(ellipse at 50% 45%, var(--label-black-soft), var(--label-black) 75%);
    color: var(--cream);
    font-family: "Roboto Slab", serif;
  }
  .frame { position: absolute; inset: 0; }
  .horse-photo {
    position: absolute; left: 190px; top: 150px; width: 180px; height: 240px;
    border-radius: 42% 42% 30% 30%;
    background: radial-gradient(ellipse at 45% 35%, var(--horse-light), var(--horse-dark) 70%);
  }
  .est, .year, .barrel-no, .alc, .strength, .single {
    position: absolute; text-align: center; font-weight: 700; line-height: 1.1;
    display: flex; flex-direction: column; justify-content: center; align-items: center;
  }
  .est { left: 50px; top: 355px; width: 85px; height: 47px; font-size: 26px; }
  .year { left: 420px; top: 290px; width: 90px; height: 55px; font-size: 28px; }
  .brand {
    position: absolute; left: 45px; right: 45px; top: 424px; text-align: center;
    font-family: "Abril Fatface", serif; font-weight: 400; font-size: 78px;
    letter-spacing: 1px; line-height: 84px;
  }
  .style {
    position: absolute; left: 0; right: 0; top: 514px; text-align: center;
    font-size: 25px; font-weight: 700; letter-spacing: 1px; line-height: 30px;
  }
  .whiskey {
    position: absolute; left: 120px; right: 120px; top: 540px; text-align: center;
    font-family: "Pinyon Script", cursive; font-size: 60px; line-height: 80px;
  }
  .alc { left: 440px; top: 560px; width: 76px; height: 60px; font-size: 12px; }
  .alc strong { font-size: 24px; }
  .barrel-no { left: 48px; top: 662px; width: 70px; height: 66px; font-size: 10px; }
  .barrel-no strong { font-size: 28px; }
  .age {
    position: absolute; left: 130px; right: 130px; top: 672px; text-align: center;
    font-weight: 700; font-size: 20px; line-height: 44px;
  }
  .age strong { font-size: 34px; color: var(--copper); }
  .strength { left: 444px; top: 662px; width: 74px; height: 66px; font-size: 13px; }
  .brand-mark {
    position: absolute; left: 215px; top: 815px; width: 130px; height: 30px;
    display: flex; justify-content: center; align-items: center; gap: 7px;
    font-weight: 700; font-size: 15px; letter-spacing: 1px;
  }
  .brand-mark .dot {
    flex: none; width: 12px; height: 12px; border-radius: 50%; background: var(--cream);
  }
  .single { left: 50px; top: 800px; width: 120px; height: 60px; font-size: 14px; }
</style>
</head>
<body>
  <section class="label">
    <svg class="frame" width="560" height="960" viewBox="0 0 560 960" fill="none" stroke="#c39a78" stroke-width="2">
      <path class="cartouche" d="M40 410 H140 Q280 200 420 410 H520 V650 H440 V760 H340 V740 H220 V760 H120 V650 H40 Z" />
      <path class="cartouche-inner" d="M132 402 Q280 186 428 402" stroke-width="1" />
      <rect x="50" y="355" width="85" height="47" />
      <rect x="420" y="290" width="90" height="55" />
      <rect x="50" y="800" width="120" height="60" />
      <circle cx="280" cy="830" r="70" stroke-width="1.5" />
      <path d="M250 512 H310" stroke-width="1" />
    </svg>
    <div class="horse-photo" role="img" aria-label="Black and white photograph of a galloping racehorse with jockey"></div>
    <div class="year">2016</div>
    <div class="est">EST</div>
    <h1 class="brand">DARKRUN</h1>
    <div class="style">STRAIGHT BOURBON</div>
    <div class="whiskey">Whiskey</div>
    <div class="alc">ALC VOL<strong>66%</strong></div>
    <div class="barrel-no">BARREL NO.<strong>28</strong></div>
    <div class="age">AGE <strong>10</strong> YRS</div>
    <div class="strength">BARREL<br>STRENGTH</div>
    <div class="brand-mark"><span class="dot"></span>DARKRUN</div>
    <div class="single">SINGLE<br>BARREL</div>
  </section>
</body>
</html>
```